Non-profit wants to save the world needs Blogwright presence

My name is Marco Estelani. I'm a photographer who started a charity (Rancho las Brisas) to help the rural schools and health clinics in Central America. We distribute schools supplies and help health clinics with much needed medical supplies and equipment. I need a way to accept donations. I need to have several different writers post to the blog (in Spanish and English). I have a domain name registered (www.rancholasbrisas.org) and started a simple wordpress site as well at http://www.rancholasbrisas.wordpress.com

Industry/Entity Type

Charity

```html
<!DOCTYPE html>
<html lang="en">
<head>
<meta charset="utf-8">
<title>Hello world! | Rancho las Brisas</title>
<link href="https://fonts.googleapis.com/css2?family=Montserrat:wght@400;600;700&family=PT+Serif:wght@400;700&family=Open+Sans:wght@400;600&family=Source+Code+Pro&display=swap" rel="stylesheet">
<style>
  :root {
    --lime: #a3e01b;
    --header: #2f2a35;
    --footer: #1f1c22;
    --ink: #333333;
    --muted: #666666;
    --accent: #3cc23c;
    --rule: #e6e6e6;
    --field: #eeeeee;
    --card: #c9d2e0;
    --white: #ffffff;
  }
  * { margin: 0; padding: 0; box-sizing: border-box; }
  html, body { width: 1200px; height: 2384px; overflow: hidden; }
  body {
    position: relative;
    background: var(--lime);
    font-family: "PT Serif", Georgia, serif;
    color: var(--ink);
  }
  .page {
    position: absolute; left: 74px; top: 0; width: 1086px; height: 2384px;
    background: var(--white);
  }
  .site-header {
    position: absolute; left: 74px; top: 0; width: 1086px; height: 127px;
    background: var(--header);
  }
  .brand {
    position: absolute; left: 14px; top: 42px;
    display: flex; align-items: center; gap: 10px;
    font-family: "Montserrat", sans-serif; font-weight: 700; font-size: 14px;
    color: var(--lime); white-space: nowrap;
  }
  .brand-dot { width: 44px; height: 44px; border-radius: 50%; background: var(--lime); flex: none; }
  .main-nav a {
    position: absolute; top: 54px;
    font-family: "Montserrat", sans-serif; font-size: 16px; letter-spacing: 2px;
    color: var(--white); text-decoration: none; white-space: nowrap;
  }
  .post-title {
    position: absolute; left: 93px; top: 172px;
    font-family: "Montserrat", sans-serif; font-weight: 600; font-size: 31px; color: #222;
  }
  .post-meta { position: absolute; left: 93px; top: 222px; font-size: 12px; color: var(--muted); }
  .post-image {
    position: absolute; left: 93px; top: 257px; width: 747px; height: 498px;
    background: radial-gradient(ellipse at 45% 45%, #4f9a5a 0%, #1f5a3a 35%, #0c2a22 70%, #061612 100%);
  }
  .post-body { position: absolute; left: 93px; top: 790px; width: 747px; font-size: 14px; line-height: 26px; color: #444; }
  .post-body p { margin-bottom: 22px; }
  .post-body blockquote {
    border-left: 5px solid var(--accent); padding: 4px 0 4px 20px; margin: 0 0 26px;
  }
  .comments-title {
    position: absolute; left: 93px; top: 1466px;
    font-family: "Montserrat", sans-serif; font-weight: 600; font-size: 28px; color: #222;
  }
  .avatar { position: absolute; left: 93px; top: 1515px; width: 86px; height: 88px; background: #d6d6d6; }
  .comment {
    position: absolute; left: 190px; top: 1512px; width: 540px;
    font-size: 13px; line-height: 22px; color: #444;
  }
  .comment .author { font-weight: 700; color: #222; }
  .comment .date { font-size: 11px; color: var(--muted); font-weight: 400; }
  .btn {
    position: absolute; border: 2px solid var(--accent); color: var(--accent); background: var(--white);
    font-family: "Open Sans", sans-serif; font-size: 18px;
    display: flex; align-items: center; justify-content: center;
  }
  .reply-btn { left: 752px; top: 1515px; width: 86px; height: 44px; }
  .submit-btn { left: 638px; top: 2217px; width: 200px; height: 48px; }
  .respond-title {
    position: absolute; left: 93px; width: 747px; top: 1672px; text-align: center;
    font-family: "Montserrat", sans-serif; font-weight: 700; font-size: 14px; letter-spacing: 3px; color: #222;
  }
  .respond-note { position: absolute; left: 93px; top: 1706px; font-size: 13px; color: var(--muted); }
  .field {
    position: absolute; left: 93px; width: 373px; background: var(--field);
    font-family: "Open Sans", sans-serif; font-size: 14px; color: #888;
    padding: 0 10px; display: flex; align-items: center;
  }
  .field-name { top: 1743px; height: 45px; }
  .field-email { top: 1801px; height: 45px; }
  .field-site { top: 1857px; height: 42px; }
  .field-comment { top: 1912px; width: 747px; height: 181px; align-items: flex-start; padding-top: 12px; }
  .field svg { position: absolute; right: 8px; top: 14px; }
  .allowed-tags {
    position: absolute; left: 93px; top: 2118px; width: 747px;
    font-size: 13px; line-height: 24px; color: #555;
  }
  .allowed-tags code { font-family: "Source Code Pro", monospace; font-size: 12px; color: #999; }
  .sidebar-rule { position: absolute; left: 895px; top: 150px; width: 1px; height: 2180px; background: var(--rule); }
  .sidebar { position: absolute; left: 914px; top: 180px; width: 230px; text-align: center; font-size: 13px; color: #444; }
  .widget-title {
    font-family: "Montserrat", sans-serif; font-weight: 700; font-size: 13px; letter-spacing: 2px; color: #222;
  }
  .recent li { list-style: none; text-align: left; padding-left: 10px; line-height: 30px; }
  .select {
    width: 180px; height: 22px; margin: 8px auto 0; border: 1px solid #aaa; border-radius: 3px;
    font-family: "Open Sans", sans-serif; font-size: 10px; text-align: left; padding: 3px 6px; position: relative;
  }
  .select::after { content: "▾"; position: absolute; right: 6px; top: 2px; }
  .donate-btn {
    width: 82px; height: 26px; margin: 14px auto 0; border-radius: 4px;
    background: var(--accent); color: var(--white);
    font-family: "Open Sans", sans-serif; font-weight: 600; font-size: 13px; line-height: 26px;
  }
  .cards { display: flex; gap: 4px; justify-content: center; margin-top: 6px; }
  .cards span { width: 18px; height: 12px; background: var(--card); border-radius: 2px; }
  .site-footer {
    position: absolute; left: 36px; top: 2342px; width: 1124px; height: 42px; background: var(--footer);
    color: #ddd; font-family: "Montserrat", sans-serif; font-size: 10px; letter-spacing: 2px;
    display: flex; align-items: center; justify-content: center;
  }
</style>
</head>
<body>
  <div class="page"></div>

  <header class="site-header">
    <div class="brand"><span class="brand-dot"></span>Rancho las Brisas</div>
    <nav class="main-nav">
      <a href="#" style="left:240px">HOME</a>
      <a href="#" style="left:358px">AUTHORS</a>
      <a href="#" style="left:504px">GALLERY</a>
      <a href="#" style="left:634px">ARTICLES 01</a>
      <a href="#" style="left:790px">ARTICLES 02</a>
      <a href="#" style="left:944px">CONTACT</a>
    </nav>
  </header>

  <article>
    <h1 class="post-title">Hello world!</h1>
    <p class="post-meta">by Tavi | Sep 22, 2014 | Uncategorized | 1 comment</p>
    <div class="post-image" role="img" aria-label="Close-up photo of green leaves and flower buds on a dark background"></div>
    <div class="post-body">
      <p>Welcome to Blogwright. This is your first post. Edit or delete it, then start blogging!</p>
      <blockquote>Lorem ipsum dolor sit amet, consectetur adipiscing elit. Praesent varius sed velit quis tempor. Fusce tincidunt sed mauris non dictum. In fringilla ultricies iaculis. Suspendisse felis dolor, posuere ut purus id, pretium ultricies dolor. Phasellus varius vitae orci at convallis. Phasellus metus ipsum, congue sit amet nisl sit</blockquote>
      <p>Lorem ipsum dolor sit amet, consectetur adipiscing elit. Praesent varius sed velit quis tempor. Fusce tincidunt sed mauris non dictum. In fringilla ultricies iaculis. Suspendisse felis dolor, posuere ut purus id, pretium ultricies dolor. Phasellus varius vitae orci at convallis. Phasellus metus ipsum, congue sit amet nisl sit amet, sagittis laoreet enim. Curabitur semper urna a gravida consequat. Fusce condimentum, velit a convallis aliquam, enim mauris consequat arcu, nec rhoncus nunc lectus a ligula. Morbi vestibulum nisi mi, at maximus arcu ultrices id. Morbi rhoncus, tellus sed venenatis dapibus, nisl felis vestibulum nulla, eget ornare orci ex id orci. Aenean lectus mi, ullamcorper vel porttitor eget, malesuada a mauris. Maecenas consequat et lacus id vestibulum. Aenean tincidunt erat et sapien porttitor, non bibendum dui mollis. Nulla urna tortor, luctus quis imperdiet ut, viverra nec augue.</p>
      <p>Aliquam pharetra cursus ex, mattis euismod dui semper a. Integer quis massa lacus. Etiam vel libero eget enim dapibus mattis imperdiet sit amet nisl. Donec ultrices convallis mi, eu venenatis urna lacinia vitae. Pellentesque sed justo scelerisque, sodales nisi eu, ultrices sem. Integer sit amet vestibulum ante, vitae ultricies ipsum. Phasellus ac elit vel nisl gravida sodales in sit amet lorem. Fusce ullamcorper condimentum feugiat. Donec blandit porttitor erat in iaculis. Donec convallis neque in luctus maximus. Pellentesque posuere quam diam, at ultrices ex dapibus id. Nulla facilisi. Donec convallis suscipit facilisis. Fusce tempus tortor magna, nec accumsan risus pharetra ac. Donec diam augue, congue vitae efficitur a, faucibus vitae felis.</p>
    </div>
  </article>

  <section class="comments">
    <h2 class="comments-title">1 Comment</h2>
    <div class="avatar"></div>
    <div class="comment">
      <p><span class="author">Mr Blogwright</span> <span class="date">on September 22, 2014 at 4:09 am</span></p>
      <p>Hi, this is a comment.<br>To delete a comment, just log in and view the post's comments. There you will have the option to edit or delete them.</p>
    </div>
    <div class="btn reply-btn">Reply</div>

    <h3 class="respond-title">SUBMIT A COMMENT</h3>
    <p class="respond-note">Your email address will not be published. Required fields are marked *</p>
    <div class="field field-name">Name *
      <svg width="16" height="16" viewBox="0 0 16 16"><path d="M3 13 L11 5 M8 4 L12 4 L12 8" stroke="#4a7fc1" stroke-width="2" fill="none"/></svg>
    </div>
    <div class="field field-email">Email *
      <svg width="16" height="16" viewBox="0 0 16 16"><path d="M3 13 L11 5 M8 4 L12 4 L12 8" stroke="#4a7fc1" stroke-width="2" fill="none"/></svg>
    </div>
    <div class="field field-site">Website</div>
    <div class="field field-comment">Comment</div>
    <p class="allowed-tags">You may use these HTML tags and attributes: <code>&lt;a href="" title=""&gt; &lt;abbr title=""&gt; &lt;acronym title=""&gt; &lt;b&gt; &lt;blockquote cite=""&gt; &lt;cite&gt; &lt;code&gt; &lt;del datetime=""&gt; &lt;em&gt; &lt;i&gt; &lt;q cite=""&gt; &lt;strike&gt; &lt;strong&gt;</code></p>
    <div class="btn submit-btn">Submit Comment</div>
  </section>

  <div class="sidebar-rule"></div>
  <aside class="sidebar">
    <h4 class="widget-title">RECENT POSTS</h4>
    <ul class="recent">
      <li>Sample Post 03</li>
      <li>Second Article</li>
      <li>Hello world!</li>
    </ul>
    <h4 class="widget-title" style="margin-top:20px">ARCHIVES</h4>
    <div class="select">Select Month</div>
    <h4 class="widget-title" style="margin-top:28px">CATEGORIES</h4>
    <div class="select">Select Category</div>
    <h4 class="widget-title" style="margin-top:28px">DONATE</h4>
    <p style="margin-top:6px">Want to help the poor, today?</p>
    <div class="donate-btn">Donate</div>
    <div class="cards"><span></span><span></span><span></span><span></span><span></span></div>
  </aside>

  <footer class="site-footer">© WEBSITE, 2014 | POWERED BY TESSEL &amp; BLOGWRIGHT</footer>
</body>
</html>
```